Small Accounting Practice needs something creative

We need a business card design for a new small accounting practice based in Perth, Australia. The name of the practice is 'Kelvarin Ledger Group Pty Ltd'. We providing Tax, Bookkeeping and Accounting services. Our target are individuals and small businesses. We want the design to be simply and creative. Also, we can the design can help us to gain people's trust.

Target Market(s)

Individuals and small businesses.

Industry/Entity Type

Accounting

Colors

Designer to choose colors to be used in the design.

```html
<!DOCTYPE html>
<html lang="en">
<head>
<meta charset="utf-8">
<title>Kelvarin Ledger Group – Business Card</title>
<link rel="stylesheet" href="https://fonts.googleapis.com/css2?family=Open+Sans:wght@400;600&family=Exo+2:wght@500;600&display=swap">
<style>
  :root {
    --backdrop: #3b3c3f;
    --card: #ffffff;
    --brand-blue: #2f8fe6;
    --ink: #2b2b2b;
    --icon: #3a3a3a;
    --on-blue: #ffffff;
  }
  * { margin: 0; padding: 0; box-sizing: border-box; }
  html, body {
    width: 1200px; height: 816px; overflow: hidden;
    background: var(--backdrop);
  }
  .card {
    position: absolute; left: 75px; top: 108px;
    width: 1050px; height: 600px;
    background: var(--card);
    border-radius: 44px;
    overflow: hidden;
    font-family: "Open Sans", Arial, sans-serif;
    color: var(--ink);
  }
  .brand {
    position: absolute; left: 520px; top: 70px;
    display: flex; align-items: center; gap: 22px;
  }
  .brand-mark {
    width: 70px; height: 70px; background: var(--brand-blue);
  }
  .brand-name {
    color: var(--brand-blue);
    font-weight: 400; font-size: 40px; line-height: 44px;
  }
  .rule {
    position: absolute; left: 420px; right: 0; top: 248px;
    height: 3px; background: var(--brand-blue);
  }
  .name-band {
    position: absolute; left: 0; top: 248px;
    width: 450px; height: 96px;
    background: var(--brand-blue);
    border-radius: 0 48px 48px 0;
    color: var(--on-blue);
    text-align: right; padding: 12px 48px 0 0;
    font-family: "Exo 2", Arial, sans-serif;
  }
  .person-name { font-size: 32px; font-weight: 600; letter-spacing: 1px; line-height: 40px; }
  .person-role { font-size: 20px; font-weight: 500; letter-spacing: 2px; line-height: 28px; }
  .address {
    position: absolute; left: 620px; top: 300px;
    display: flex; gap: 16px; font-size: 22px; line-height: 32px;
  }
  .contacts {
    position: absolute; left: 60px; top: 410px;
    list-style: none; font-size: 22px; line-height: 44px;
  }
  .contacts li, .address { align-items: flex-start; }
  .contacts li { display: flex; align-items: center; gap: 18px; }
  .icon { width: 22px; height: 22px; fill: var(--icon); flex: none; }
  .address .icon { margin-top: 5px; }
</style>
</head>
<body>
  <div class="card">
    <div class="brand">
      <div class="brand-mark"></div>
      <div class="brand-name">Kelvarin Ledger<br>Group</div>
    </div>

    <div class="rule"></div>

    <div class="name-band">
      <div class="person-name">Daniel Harwood</div>
      <div class="person-role">GENERAL MANAGER</div>
    </div>

    <div class="address">
      <svg class="icon" viewBox="0 0 24 24" aria-hidden="true"><path d="M12 3 1 12h3v9h6v-6h4v6h6v-9h3z"/></svg>
      <div>48 Ardent Lane,<br>Perth WA, Australia</div>
    </div>

    <ul class="contacts">
      <li>
        <svg class="icon" viewBox="0 0 24 24" aria-hidden="true"><path d="M6.6 10.8a15.1 15.1 0 0 0 6.6 6.6l2.2-2.2c.3-.3.7-.4 1-.2 1.1.4 2.3.6 3.6.6.6 0 1 .4 1 1V20c0 .6-.4 1-1 1A17 17 0 0 1 3 4c0-.6.4-1 1-1h3.5c.6 0 1 .4 1 1 0 1.3.2 2.5.6 3.6.1.3 0 .7-.2 1z"/></svg>
        <span>+61 (08) 9555 0142</span>
      </li>
      <li>
        <svg class="icon" viewBox="0 0 24 24" aria-hidden="true"><path d="M2 5h20v14H2zm2 2v.5l8 5 8-5V7z"/></svg>
        <span>hello@kelvarinledger.com</span>
      </li>
      <li>
        <svg class="icon" viewBox="0 0 24 24" aria-hidden="true"><path d="M12 2a10 10 0 1 0 0 20 10 10 0 0 0 0-20zm6.9 6h-3a15 15 0 0 0-1.3-3.9A8 8 0 0 1 18.9 8zM12 4c.8 1.2 1.5 2.5 1.9 4h-3.8c.4-1.5 1.1-2.8 1.9-4zM4.3 14a8 8 0 0 1 0-4h3.4a16 16 0 0 0 0 4zm.8 2h3a15 15 0 0 0 1.3 3.9A8 8 0 0 1 5.1 16zm3-8h-3a8 8 0 0 1 4.3-3.9C8.8 5.3 8.4 6.6 8.1 8zM12 20c-.8-1.2-1.5-2.5-1.9-4h3.8c-.4 1.5-1.1 2.8-1.9 4zm2.3-6H9.7a14 14 0 0 1 0-4h4.6a14 14 0 0 1 0 4zm.3 5.9c.6-1.2 1-2.5 1.3-3.9h3a8 8 0 0 1-4.3 3.9zm1.7-5.9a16 16 0 0 0 0-4h3.4a8 8 0 0 1 0 4z"/></svg>
        <span>www.kelvarinledger.com</span>
      </li>
    </ul>
  </div>
</body>
</html>
```